Commercial New Construction and Remodeling

Residential New Construction and Remodeling

Target Market(s)

Commercial and residential, Investors

I would like you to know that I'm planning to use transparent (clear) business cards. The Logo could have colors like gray, white, lemon green.
Or another combination could be gray, white and some color between mustard or sand.

Requirements
Must have
• The Logo could be letters like HBP. I don't have preference where the Logo is on the card. And somewhere on the card the full name appears.

NAME OF THE COMPANY: HARBOR BUILDING PARTNERS
Nice to have
• I like the minimalist look,Geometric figures.

```html
<!DOCTYPE html>
<html lang="en">
<head>
<meta charset="utf-8">
<title>Harbor Building Partners – Business Card</title>
<link rel="stylesheet" href="https://fonts.googleapis.com/css2?family=Montserrat:wght@600;700&family=Poppins:wght@300;500&family=Open+Sans:ital,wght@1,600&display=swap">
<style>
  :root {
    --page-bg: #dde3e8;
    --card-light: #f3f5f5;
    --card-dark: #5c5f61;
    --card-dark-deep: #4e5153;
    --lime: #8cbf2f;
    --lime-deep: #76a824;
    --gray-text: #6e7173;
    --light-text: #ffffff;
    --soft-text: #d9dcdd;
  }
  * { margin: 0; padding: 0; box-sizing: border-box; }
  html, body {
    width: 1200px; height: 900px; overflow: hidden;
    background: var(--page-bg);
  }
  .card {
    position: absolute; left: 120px; top: 178px;
    width: 960px; height: 544px;
    border-radius: 20px; overflow: hidden;
    background: var(--card-light);
    box-shadow: 0 12px 34px rgba(40, 50, 60, 0.18);
  }
  .card-shapes { position: absolute; inset: 0; }
  .holder { position: absolute; left: 55px; top: 70px; color: var(--light-text); }
  .holder-name {
    font: 700 21px/1.2 "Montserrat", sans-serif; letter-spacing: 1.5px;
  }
  .holder-title {
    font: 600 14px/1.2 "Montserrat", sans-serif; letter-spacing: 0.8px; margin-top: 6px;
  }
  .contact {
    position: absolute; left: 55px;
    font: 300 19px/29px "Poppins", sans-serif; color: var(--soft-text);
    display: flex; gap: 12px;
  }
  .contact svg { flex: none; margin-top: 6px; }
  .contact-area { top: 350px; }
  .contact-direct { top: 440px; }
  .brand {
    position: absolute; left: 480px; width: 440px; top: 70px;
    text-align: center; color: var(--gray-text);
  }
  .brand-initials {
    font: 700 78px/1 "Montserrat", sans-serif; letter-spacing: 4px;
    color: var(--gray-text);
  }
  .brand-name {
    font: 700 30px/1.15 "Montserrat", sans-serif; color: var(--lime);
    margin-top: 20px;
  }
  .brand-name-row { display: flex; align-items: center; justify-content: center; gap: 12px; }
  .brand-rule { width: 70px; height: 2px; background: var(--gray-text); }
  .brand-tagline {
    font: italic 600 20px/1.2 "Open Sans", sans-serif; color: var(--gray-text);
    margin-top: 12px;
  }
  .services {
    position: absolute; right: 48px; top: 440px; list-style: none;
    font: 500 19px/29px "Poppins", sans-serif; color: var(--gray-text);
    text-align: right;
  }
  .services li::before {
    content: ""; display: inline-block; width: 10px; height: 10px;
    border-radius: 50%; background: var(--lime); margin-right: 8px; vertical-align: 2px;
  }
</style>
</head>
<body>
  <article class="card">
    <svg class="card-shapes" width="960" height="544" viewBox="0 0 960 544">
      <defs>
        <linearGradient id="darkPanel" x1="0" y1="0" x2="0" y2="1">
          <stop offset="0" stop-color="var(--card-dark)"/>
          <stop offset="1" stop-color="var(--card-dark-deep)"/>
        </linearGradient>
      </defs>
      <path class="dark-panel" fill="url(#darkPanel)" d="M0,0 H353 C375,250 560,470 757,544 H0 Z"/>
      <path class="accent-arc" fill="var(--lime)" d="M353,0 H393 C408,250 580,460 757,544 C560,470 375,250 353,0 Z"/>
    </svg>

    <header class="holder">
      <h1 class="holder-name">MATEO (TEO) RIVERA</h1>
      <p class="holder-title">MANAGING DIRECTOR</p>
    </header>

    <div class="contact contact-area">
      <svg width="14" height="19" viewBox="0 0 14 19"><path fill="var(--lime)" d="M7 0a7 7 0 0 0-7 7c0 5 7 12 7 12s7-7 7-12a7 7 0 0 0-7-7zm0 9.6A2.6 2.6 0 1 1 7 4.4a2.6 2.6 0 0 1 0 5.2z"/></svg>
      <p>Serving Austin Area<br>&amp; surroundings.</p>
    </div>

    <div class="contact contact-direct">
      <svg width="15" height="15" viewBox="0 0 24 24"><path fill="var(--lime)" d="M6.6 10.8a15.1 15.1 0 0 0 6.6 6.6l2.2-2.2a1 1 0 0 1 1-.25 11.4 11.4 0 0 0 3.6.57 1 1 0 0 1 1 1V20a1 1 0 0 1-1 1A17 17 0 0 1 3 4a1 1 0 0 1 1-1h3.5a1 1 0 0 1 1 1c0 1.25.2 2.45.57 3.57a1 1 0 0 1-.25 1z"/></svg>
      <p>512.555.0147<br>mrivera@hbpartners.net</p>
    </div>

    <section class="brand">
      <p class="brand-initials">HBP</p>
      <div class="brand-name">
        <p>HARBOR BUILDING</p>
        <div class="brand-name-row"><span class="brand-rule"></span><span>PARTNERS</span><span class="brand-rule"></span></div>
      </div>
      <p class="brand-tagline">If you can dream it, we can build it</p>
    </section>

    <ul class="services">
      <li>Commercial</li>
      <li>Residential</li>
    </ul>
  </article>
</body>
</html>
```